UPDATE 2: I HAVE ATTACHED TWO PHOTOS; PLEASE CONSIDER USING EITHER ONE IN A NEW DESIGN. THANK YOU.
UPDATE: I HAVE INCLUDED 4 SAMPLE BOOK COVERS THAT I LIKE TO HELP YOU ORIENT YOUR DESIGN WORK
Looking for book cover, spine, and back for a MEMOIR. Details:
TITLE: Mama's Quiet Orchard
AUTHOR: Lorivel Brashton
GENRE: Memoir
STYLE REQUESTED: Abstract and colorful; designers are welcome to get creative. Note that the memoir takes place largely in a poor African American city.
BOOK SUMMARY: As a young girl, Lorivel Brashton—or “Rivvy” to her friends and family—discovers the man she thought was her father wasn’t, and her real biological father wants little if anything to do with her. What follows is the story of a girl’s longing, a longing disturbed by abuse, disappointment, and loneliness.
Set against the backdrop of Gary, Indiana—the then “murder capital of the world”—Mama’s Quiet Orchard follows Lorivel as she searches and grows, following a path that eventually leads her to self-discovery and self-confidence.
Template provided for InDesign. Please note margins and bleed areas. Make sure any letters/words are at least one inch from edges. On spine, leave three inches at bottom for publisher's logo.
Updates
To all designers: Please note that there should NOT be any images of people as part of your designs. Thank you, and my apologies for not mentioning that in the initial ask.

```html
<!DOCTYPE html>
<html lang="en">
<head>
<meta charset="utf-8">
<title>Mama's Quiet Orchard — Lorivel Brashton</title>
<link rel="stylesheet" href="https://fonts.googleapis.com/css2?family=Bebas+Neue&family=Montserrat:wght@600&display=swap">
<style>
  :root {
    --page: #ffffff;
    --mist-top: #f5f4f0;
    --mist-mid: #e9e8e4;
    --mist-low: #dcdbd7;
    --pier-light: #8e8e8b;
    --pier-mid: #5e5e5c;
    --pier-dark: #262626;
    --ink: #0d0d0d;
    --author: #f1f0ec;
  }
  html, body {
    margin: 0;
    padding: 0;
    width: 1200px;
    height: 1200px;
    overflow: hidden;
    background: var(--page);
  }
  .book-cover {
    position: absolute;
    left: 261px;
    top: 91px;
    width: 685px;
    height: 1025px;
    overflow: hidden;
  }
  .cover-photo {
    position: absolute;
    inset: 0;
    width: 685px;
    height: 1025px;
    display: block;
  }
  .genre-label {
    position: absolute;
    top: 59px;
    left: 0;
    right: 0;
    margin: 0;
    text-align: center;
    font-family: "Montserrat", sans-serif;
    font-weight: 600;
    font-size: 22px;
    line-height: 22px;
    letter-spacing: 2px;
    color: var(--ink);
  }
  .book-title {
    position: absolute;
    top: 108px;
    left: 0;
    right: 0;
    margin: 0;
    text-align: center;
    font-family: "Bebas Neue", sans-serif;
    font-weight: 400;
    font-size: 172px;
    line-height: 139px;
    letter-spacing: 1px;
    color: var(--ink);
  }
  .book-title span { display: block; }
  .author-name {
    position: absolute;
    top: 943px;
    left: 0;
    right: 0;
    margin: 0;
    text-align: center;
    font-family: "Bebas Neue", sans-serif;
    font-weight: 400;
    font-size: 36px;
    line-height: 36px;
    letter-spacing: 14px;
    padding-left: 14px;
    color: var(--author);
  }
</style>
</head>
<body>
  <article class="book-cover">
    <svg class="cover-photo" viewBox="0 0 685 1025" role="img" aria-label="Black and white photograph of a weathered wooden pier stretching into thick fog">
      <defs>
        <linearGradient id="fog" x1="0" y1="0" x2="0" y2="1">
          <stop offset="0" stop-color="var(--mist-mid)"/>
          <stop offset="0.25" stop-color="var(--mist-top)"/>
          <stop offset="0.8" stop-color="var(--mist-low)"/>
          <stop offset="1" stop-color="var(--pier-mid)"/>
        </linearGradient>
        <linearGradient id="pier" x1="0" y1="0" x2="0" y2="1">
          <stop offset="0" stop-color="var(--pier-light)"/>
          <stop offset="0.6" stop-color="var(--pier-mid)"/>
          <stop offset="1" stop-color="var(--pier-dark)"/>
        </linearGradient>
      </defs>
      <rect width="685" height="1025" fill="url(#fog)"/>
      <polygon points="137,557 543,557 685,903 685,1025 40,1025" fill="url(#pier)"/>
    </svg>
    <p class="genre-label">MEMOIR</p>
    <h1 class="book-title">
      <span>MAMA'S</span>
      <span>QUIET</span>
      <span>ORCHARD</span>
    </h1>
    <p class="author-name">LORIVEL BRASHTON</p>
  </article>
</body>
</html>
```